Printed Promo Flyer for new pet business

We need a double sided flyer design as per the given example flyer, just better looking and more fun.Flyers will need to be printed.Flyer size approx 10.5cm x 15cm. The text will need to be amended slightly afterwards to be more fun unless you can create a new tone of voice as well (should sound fun like breezy do it) Look and Feel: emotional, fun, loving, professional
See attached files.

Target Market(s)

Pet owners in the UK who want the convenience of getting their pets parasite treatment delivered to their door without the need of having to run to the vet or store for purchase

Industry/Entity Type

Pet Care

Colors
00a990
6b449b

Requirements
Must have
• all the content context as given in the example flyer.
Nice to have
• Tone of voice can be changed to be more fun (using Breezy as a guide)

```html
<!DOCTYPE html>
<html lang="en">
<head>
<meta charset="utf-8">
<title>Snug Paws Box – Promo Flyer</title>
<link href="https://fonts.googleapis.com/css2?family=Fira+Sans+Extra+Condensed:ital,wght@0,400;0,700;1,400;1,700;1,800&family=Nunito:ital,wght@1,800;1,900&display=swap" rel="stylesheet">
<style>
  :root {
    --teal: #02a9b5;
    --teal-light: #1cb8c4;
    --teal-deep: #0ea3b0;
    --purple: #7e5ba8;
    --yellow: #fbb817;
    --white: #ffffff;
    --ink: #1d1d1f;
    --backdrop: #3a3a3a;
    --cond: "Fira Sans Extra Condensed", sans-serif;
    --heading: "Nunito", sans-serif;
  }
  html, body {
    margin: 0;
    width: 1200px;
    height: 1200px;
    overflow: hidden;
    background: var(--backdrop);
  }
  .stage {
    position: absolute;
    left: 0; top: 0;
    width: 1932px;
    height: 1932px;
    transform: scale(0.621118);
    transform-origin: 0 0;
  }
  .flyer {
    position: absolute;
    top: 389px;
    width: 811px;
    height: 1159px;
    box-shadow: 6px 8px 14px rgba(0,0,0,0.45);
  }
  .flyer svg { display: block; width: 811px; height: 1159px; }
  .flyer--front { left: 132px; }
  .flyer--back { left: 1013px; }

  .highlight {
    font-family: var(--cond);
    font-style: italic;
    font-weight: 700;
    fill: var(--purple);
    stroke: var(--yellow);
    stroke-linejoin: round;
    paint-order: stroke;
  }
  .brand-name {
    font-family: var(--cond);
    font-weight: 700;
    fill: var(--purple);
    letter-spacing: 4px;
  }
  .card-title {
    font-family: var(--heading);
    font-style: italic;
    font-weight: 900;
    font-size: 30px;
    fill: var(--ink);
  }
  .card-body {
    font-family: var(--cond);
    font-weight: 400;
    font-size: 23px;
    fill: var(--ink);
  }
  .step {
    font-family: var(--cond);
    font-size: 23px;
    fill: var(--white);
  }
  .step-num { font-weight: 700; font-style: italic; fill: var(--yellow); }
  .offer-label {
    font-family: var(--cond);
    font-style: italic;
    font-weight: 700;
    font-size: 48px;
    fill: var(--white);
  }
  .price {
    font-family: var(--cond);
    font-style: italic;
    font-weight: 800;
    fill: var(--purple);
    stroke: var(--white);
    stroke-linejoin: round;
    paint-order: stroke;
  }
  .web-address {
    font-family: var(--cond);
    font-style: italic;
    font-weight: 700;
    font-size: 40px;
    fill: var(--white);
  }
  .icon-badge { fill: var(--purple); stroke: var(--white); stroke-width: 7; }
  .icon-line { fill: none; stroke: var(--white); stroke-width: 6; stroke-linecap: round; stroke-linejoin: round; }
</style>
</head>
<body>
<main class="stage">

  <!-- Front side -->
  <section class="flyer flyer--front">
    <svg viewBox="0 0 811 1159" xmlns="http://www.w3.org/2000/svg">
      <defs>
        <linearGradient id="photo-tones" x1="0" y1="0" x2="1" y2="1">
          <stop offset="0" stop-color="#c9cfc6"/>
          <stop offset="0.35" stop-color="#5f6b3f"/>
          <stop offset="0.7" stop-color="#3d4a2c"/>
          <stop offset="1" stop-color="#25366e"/>
        </linearGradient>
      </defs>
      <rect class="front-base" width="811" height="1159" fill="var(--teal)"/>
      <path class="front-white-wave" fill="var(--white)"
        d="M190 0 L605 0 C670 100 672 250 675 380 C680 480 720 560 811 610 L811 1159 L0 1159 L0 470 C130 440 300 470 445 505 C340 420 240 360 200 250 C180 180 185 80 190 0Z"/>
      <path class="front-purple-wave" fill="var(--purple)"
        d="M605 0 L811 0 L811 610 C720 560 680 480 675 380 C672 250 670 100 605 0Z"/>
      <path class="front-teal-frame" fill="var(--teal)"
        d="M0 470 C200 440 400 470 520 600 C620 720 640 900 600 1020 C580 1090 540 1130 510 1159 L0 1159Z"/>
      <path class="front-photo" role="img" aria-label="Photo: a smiling woman hugging a happy labrador in a woodland setting"
        fill="url(#photo-tones)"
        d="M0 490 C180 460 360 490 470 600 C560 700 580 880 540 1000 C520 1070 490 1120 470 1159 L0 1159Z"/>

      <g class="brand-lockup">
        <circle cx="445" cy="130" r="34" fill="var(--teal)"/>
        <text class="brand-name" x="445" y="254" font-size="72" text-anchor="middle">SNUG PAWS</text>
        <text class="brand-name" x="445" y="312" font-size="52" text-anchor="middle">BOX</text>
      </g>

      <g class="front-headline">
        <text class="highlight" x="413" y="588" font-size="94" stroke-width="30" textLength="260" lengthAdjust="spacingAndGlyphs">The best</text>
        <text class="highlight" x="408" y="680" font-size="94" stroke-width="30" textLength="332" lengthAdjust="spacingAndGlyphs">protection</text>
        <text class="highlight" x="411" y="770" font-size="94" stroke-width="30" textLength="269" lengthAdjust="spacingAndGlyphs">and care</text>
        <text class="highlight" x="408" y="1042" font-size="66" stroke-width="24" textLength="275" lengthAdjust="spacingAndGlyphs">For your pet</text>
      </g>
    </svg>
  </section>

  <!-- Back side -->
  <section class="flyer flyer--back">
    <svg viewBox="0 0 811 1159" xmlns="http://www.w3.org/2000/svg">
      <rect class="back-base" width="811" height="1159" fill="var(--teal)"/>
      <path class="back-soft-wave" fill="var(--teal-light)"
        d="M200 0 L605 0 C660 80 680 200 680 330 C690 470 740 560 811 620 L811 1035 L560 1020 C600 900 560 780 430 690 C300 600 220 500 195 360 C175 240 180 100 200 0Z"/>
      <path class="back-deep-wave" fill="var(--teal-deep)"
        d="M605 0 L811 0 L811 620 C740 560 690 470 680 330 C680 200 660 80 605 0Z"/>

      <text class="highlight" x="62" y="172" font-size="64" stroke-width="26" textLength="362" lengthAdjust="spacingAndGlyphs">why snug paws box?</text>

      <g class="benefit-cards">
        <rect x="60" y="255" width="343" height="171" fill="var(--white)"/>
        <rect x="425" y="255" width="343" height="171" fill="var(--white)"/>
        <rect x="60" y="450" width="343" height="170" fill="var(--white)"/>
        <rect x="425" y="450" width="343" height="170" fill="var(--white)"/>

        <text class="card-title" x="105" y="307" textLength="246" lengthAdjust="spacingAndGlyphs">Protection &amp; Care</text>
        <text class="card-body" x="105" y="343" textLength="278" lengthAdjust="spacingAndGlyphs">Protection against all major parasites</text>
        <text class="card-body" x="105" y="373" textLength="256" lengthAdjust="spacingAndGlyphs">to avoid putting your pet and your</text>
        <text class="card-body" x="105" y="403" textLength="96" lengthAdjust="spacingAndGlyphs">family at risk</text>

        <text class="card-title" x="503" y="316" textLength="101" lengthAdjust="spacingAndGlyphs">In Time</text>
        <text class="card-body" x="503" y="352" textLength="194" lengthAdjust="spacingAndGlyphs">Neve having to remember</text>
        <text class="card-body" x="503" y="382" textLength="167" lengthAdjust="spacingAndGlyphs">when to treat your pet</text>

        <text class="card-title" x="140" y="505" textLength="160" lengthAdjust="spacingAndGlyphs">Convenient</text>
        <text class="card-body" x="140" y="541" textLength="187" lengthAdjust="spacingAndGlyphs">Delivered directly to your</text>
        <text class="card-body" x="140" y="571" textLength="71" lengthAdjust="spacingAndGlyphs">letter box</text>

        <text class="card-title" x="509" y="510" textLength="120" lengthAdjust="spacingAndGlyphs">Low cost</text>
        <text class="card-body" x="509" y="546" textLength="236" lengthAdjust="spacingAndGlyphs">All the high end, trusted brands</text>
        <text class="card-body" x="509" y="576" textLength="182" lengthAdjust="spacingAndGlyphs">but chraper than the vet</text>
      </g>

      <g class="benefit-icons">
        <circle class="icon-badge" cx="65" cy="266" r="32"/>
        <ellipse cx="65" cy="271" rx="12" ry="15" fill="var(--white)"/>
        <path class="icon-line" d="M50 262 H80 M50 276 H80 M58 252 L54 246 M72 252 L76 246" stroke-width="4"/>

        <circle class="icon-badge" cx="442" cy="266" r="32"/>
        <path class="icon-line" d="M442 244 V268 L454 282"/>

        <circle class="icon-badge" cx="67" cy="472" r="32"/>
        <rect x="51" y="457" width="32" height="30" rx="3" fill="var(--white)"/>
        <rect x="60" y="463" width="14" height="5" fill="var(--purple)"/>

        <circle class="icon-badge" cx="442" cy="467" r="32"/>
        <text x="442" y="482" font-family="var(--cond)" font-size="42" font-weight="700" fill="var(--white)" text-anchor="middle">£</text>
      </g>

      <text class="highlight" x="75" y="751" font-size="64" stroke-width="26" textLength="267" lengthAdjust="spacingAndGlyphs">How it works</text>
      <g class="steps">
        <text class="step" x="60" y="811" textLength="293" lengthAdjust="spacingAndGlyphs"><tspan class="step-num">1.</tspan>Select which pet the treatment is for</text>
        <text class="step" x="60" y="840" textLength="229" lengthAdjust="spacingAndGlyphs"><tspan class="step-num">2.</tspan>Choose your treatment type</text>
        <text class="step" x="60" y="870" textLength="224" lengthAdjust="spacingAndGlyphs"><tspan class="step-num">3.</tspan>Select your preferred brand</text>
        <text class="step" x="60" y="899" textLength="407" lengthAdjust="spacingAndGlyphs"><tspan class="step-num">4.</tspan>Choose between 1, 3, 6 or 12 months treatment box</text>
      </g>

      <g class="offer">
        <text class="offer-label" x="600" y="711" textLength="147" lengthAdjust="spacingAndGlyphs">Frist box</text>
        <text class="price" x="532" y="922" font-size="270" stroke-width="22">5.</text>
        <text class="price" x="664" y="820" font-size="112" stroke-width="16">99</text>
      </g>

      <path class="back-footer-band" fill="var(--purple)"
        d="M0 1056 C250 1025 560 1022 811 1052 L811 1159 L0 1159Z"/>
      <text class="web-address" x="237" y="1093" textLength="340" lengthAdjust="spacingAndGlyphs">www.snugpawsbox.co.uk</text>
    </svg>
  </section>

</main>
</body>
</html>
```